Book Cover for: TITLE Mend the Quiet Hours SUBTITLE for couples who still choose each other

We need a full cover design for a book on relationships written by husband and wife team, Marla and Walter Dunmore, PhD. This book will offer hope for couples that are on the verge of breaking up but want to work things out and stay together. The theme is to teach couples about their own reactions to their partner, how moods affect a relationship, how to get creative to solving problems and how to have a good feeling towards your partner regardless of differences. This book is about hope. It is a positive look at relationships that feel hopeless.

Target Market(s)

Married or couples that are going through a difficult time and are considering splitting up due to, communication difficulties, addiction, affair. We imagine the book will appeal to women more than men but still want a cover that men would be comfortable picking up.

Colors

Designer to choose colors to be used in the design.

Requirements
Must have
• We want the cover to beautiful, intriguing, simple and uncomplicated. We don't want it overly busy, technical, or complex.
Nice to have
• MAYBE?? a broken heart being put back together.
Should not have
• No photo, no cartoon, no flowers, no couple (unless obscure and not gender specific).

```html
<!DOCTYPE html>
<html lang="en">
<head>
<meta charset="utf-8">
<title>Mend the Quiet Hours – Book Cover</title>
<link rel="stylesheet" href="https://fonts.googleapis.com/css2?family=Anton&family=Roboto+Condensed:wght@500&family=Libre+Baskerville:wght@700&display=swap">
<style>
  :root {
    --stage: #e6e6e6;
    --sky-deep: #2f6db2;
    --sky-mid: #4a86c8;
    --sky-pale: #b9d3f0;
    --heart-glow: #dbe8fb;
    --band: #ffffff;
    --ink: #111111;
    --author: #ffffff;
  }
  * { margin: 0; padding: 0; box-sizing: border-box; }
  html, body {
    width: 1200px;
    height: 960px;
    overflow: hidden;
    background: var(--stage);
  }
  .cover {
    position: absolute;
    left: 292px;
    top: 40px;
    width: 616px;
    height: 880px;
    overflow: hidden;
    background: var(--sky-deep);
  }
  .cover-art {
    position: absolute;
    inset: 0;
    background:
      radial-gradient(ellipse 44% 30% at 52% 44%, var(--heart-glow) 0%, var(--sky-pale) 45%, rgba(185,211,240,0) 100%),
      linear-gradient(180deg, var(--sky-mid) 0%, var(--sky-deep) 100%);
  }
  .title {
    position: absolute;
    left: 0;
    right: 0;
    top: 250px;
    text-align: center;
    font-family: "Anton", "Impact", sans-serif;
    font-weight: 400;
    color: var(--ink);
    text-transform: uppercase;
    line-height: 0.95;
  }
  .title-line-main {
    display: block;
    font-size: 116px;
    letter-spacing: 1px;
  }
  .title-line-sub {
    display: block;
    font-size: 78px;
    letter-spacing: 1px;
  }
  .subtitle-band {
    position: absolute;
    left: 0;
    right: 0;
    top: 592px;
    height: 108px;
    background: var(--band);
    display: flex;
    align-items: center;
    justify-content: center;
  }
  .subtitle {
    font-family: "Roboto Condensed", "Arial Narrow", sans-serif;
    font-weight: 500;
    font-size: 30px;
    color: var(--ink);
    white-space: nowrap;
  }
  .authors {
    position: absolute;
    left: 0;
    right: 0;
    top: 770px;
    text-align: center;
    font-family: "Libre Baskerville", "Georgia", serif;
    font-weight: 700;
    font-size: 30px;
    color: var(--author);
    white-space: nowrap;
  }
</style>
</head>
<body>
  <main class="cover">
    <div class="cover-art" role="img" aria-label="Illustration of a glossy pale-blue heart wrapped in swirling rainbow smoke of pink, blue, yellow and orange, set against a blue sky with white clouds"></div>
    <h1 class="title">
      <span class="title-line-main">Mend the</span>
      <span class="title-line-sub">Quiet Hours</span>
    </h1>
    <div class="subtitle-band">
      <p class="subtitle">for couples who still choose each other</p>
    </div>
    <p class="authors">Marla &amp; Walter Dunmore</p>
  </main>
</body>
</html>
```